"Velvet Crest" sexual performance enhancement pill bottle label needed.

This should be interesting...

I am starting a line of sexual performance enhancement products. This will be the first of several products basically. Keep in mind, I am the type of business person to stay with one company for years if they provide me with quality work.

This particular product is a male sexual performance pill. The name of the product is "Velvet Crest." The packaging of the pills are a black bottle with a white top. Label on the product example would be perfect but at a minimum I have attached a "template" for your guidance.

Some of the technical aspects of this are as follows:

-File Format: Illustrator CS6 is preferred. (Winner must provide artwork in layer and can not flatten artwork.)
-Resolution: 300 dpi minimum
-Bleed: 1/16th (0.0625") inch from edge of label
-Color Mode: CMYK only or must be converted to CMYK for final production

Lastly, this is your project as a designer, artist, creator, this is essentially a piece of you that will be sold and known by thousands of people. I have no color scheme that I prefer, just use the template and follow the layout. If you have any further questions, please feel free to contact me at any time.
Updates

Quick note on the product and what it does: -Powerful, long lasting, harder erections -Works in a minutes and last for hours -Enhances sexual desire and drive Thank you for your ideas...

Project Deadline Extended
Reason: We decided to extent the project for a few more days to let the last few concepts come in. So far things are looking really good and we definitely have seen some amazing designs. Thank you for your hard work and amazing creativity. Looking forward to seeing what we have come in the next couple of day. Very respectfully, Brock

ONLY THREE DAYS LEFT!!!! Please submit your ideas as soon as possible. And as always, thank you for your help!!! V/r, Brock

Industry/Entity Type

Graphic Design

```html
<!DOCTYPE html>
<html lang="en">
<head>
<meta charset="utf-8">
<title>Velvet Crest – Label</title>
<link rel="stylesheet" href="https://fonts.googleapis.com/css2?family=Anton&family=Oswald:wght@600&family=Roboto+Condensed:wght@400&display=swap">
<style>
  :root {
    --page: #ffffff;
    --label-black: #050505;
    --hero-white: #ffffff;
    --hero-grey: #b9b9b9;
    --ink: #161616;
    --claim-white: #f4f4f4;
    --claim-grey: #6d6d6d;
    --accent-red: #e0202e;
    --rule-grey: #8a8a8a;
    --seal-gold: #d9a227;
  }
  * { margin: 0; padding: 0; box-sizing: border-box; }
  html, body {
    width: 1200px;
    height: 970px;
    overflow: hidden;
    background: var(--page);
  }
  .canvas {
    position: relative;
    width: 1200px;
    height: 970px;
  }
  .label {
    position: absolute;
    left: 80px;
    top: 166px;
    width: 1040px;
    height: 638px;
    background: var(--label-black);
    overflow: hidden;
  }
  .hero {
    position: absolute;
    left: 255px;
    top: 0;
    width: 785px;
    height: 332px;
    background: linear-gradient(90deg, var(--label-black) 0%, var(--hero-grey) 38%, var(--hero-white) 62%, var(--hero-white) 100%);
  }
  .hero-photo {
    position: absolute;
    left: 0;
    top: 0;
    width: 300px;
    height: 332px;
    background: linear-gradient(90deg, #0a0a0a 0%, #3a3a3a 45%, #d8d8d8 100%);
  }
  .product-name {
    position: absolute;
    left: 530px;
    top: 18px;
    font-family: "Oswald", sans-serif;
    font-weight: 600;
    color: var(--ink);
    font-size: 128px;
    line-height: 140px;
    letter-spacing: 1px;
    text-transform: uppercase;
  }
  .seal {
    position: absolute;
    left: 162px;
    top: 139px;
    width: 140px;
    height: 140px;
  }
  .claims {
    position: absolute;
    left: 0;
    top: 370px;
    width: 1040px;
    display: flex;
  }
  .claims-benefits {
    width: 528px;
    text-align: right;
    font-family: "Roboto Condensed", sans-serif;
    font-weight: 400;
    font-size: 54px;
    line-height: 60px;
    color: var(--claim-white);
    text-transform: uppercase;
  }
  .claims-effects {
    padding-left: 14px;
    font-family: "Anton", sans-serif;
    font-size: 54px;
    line-height: 60px;
    letter-spacing: 3px;
    color: var(--claim-grey);
    text-transform: uppercase;
  }
  .rule {
    position: absolute;
    left: 0;
    top: 566px;
    width: 1040px;
    height: 3px;
    background: var(--rule-grey);
  }
  .tagline {
    position: absolute;
    left: 0;
    top: 588px;
    width: 1040px;
    text-align: center;
    font-family: "Roboto Condensed", sans-serif;
    font-size: 28px;
    color: var(--accent-red);
    text-transform: uppercase;
  }
</style>
</head>
<body>
<div class="canvas">
  <section class="label">
    <div class="hero">
      <div class="hero-photo" role="img" aria-label="Black and white photograph of a couple about to kiss"></div>
    </div>
    <svg class="seal" viewBox="0 0 140 140" aria-hidden="true">
      <circle cx="70" cy="70" r="68" fill="var(--seal-gold)"/>
    </svg>
    <h1 class="product-name">Velvet<br>Crest</h1>
    <div class="claims">
      <p class="claims-benefits">Powerful<br>Long lasting<br>Harder erections</p>
      <p class="claims-effects">Enhances<br>Sexual desire<br>And drive</p>
    </div>
    <div class="rule"></div>
    <p class="tagline">Works in a minutes and last for hours</p>
  </section>
</div>
</body>
</html>
```